A flyer for future customers to get acquainted with our company

The flyer/card is intended for intermediaries. The purpose of this flyer is to introduce businesses to Dovrel.

It should convey: real estate and financing, with actual images. Various keywords describing what we do: project financing, temporary real estate financing, real estate financing, investment properties, transformations. We distinguish ourselves by being fast, flexible, and personal.

Please ensure the front has an attractive and inviting appearance, and leave space on the back for additional text.

Color codes: #E85B35 en #091E33

```html
<!DOCTYPE html>
<html lang="en">
<head>
<meta charset="utf-8">
<title>Dovrel – Real Estate Financing Flyer</title>
<link href="https://fonts.googleapis.com/css2?family=Poppins:wght@500;600;800&display=swap" rel="stylesheet">
<style>
  :root {
    --orange: #E85B35;
    --navy: #091E33;
    --navy-soft: #1f3a5c;
    --teal: #8fc4c4;
    --white: #ffffff;
    --backdrop: #ababab;
  }
  * { margin: 0; padding: 0; box-sizing: border-box; }
  html, body { width: 1200px; height: 800px; overflow: hidden; }
  body {
    background: var(--backdrop);
    font-family: "Poppins", sans-serif;
    position: relative;
  }
  .card {
    position: absolute;
    top: 204px;
    width: 560px;
    height: 392px;
    overflow: hidden;
    box-shadow: 0 10px 24px rgba(0,0,0,.25);
    background: var(--navy);
  }
  .card--front { left: 30px; }
  .card--back { left: 610px; }
  .card__art { position: absolute; inset: 0; }

  .brand-tab {
    position: absolute;
    left: 26px; top: 46px;
    width: 132px; height: 52px;
    background: var(--white);
    border-right: 5px solid var(--orange);
    border-bottom: 3px solid var(--orange);
    border-radius: 0 0 18px 0;
    display: flex; align-items: center; justify-content: center; gap: 6px;
  }
  .brand-tab__dot {
    width: 8px; height: 8px; border-radius: 50%;
    background: var(--orange);
  }
  .brand-tab__name {
    font-weight: 600; font-size: 24px; color: var(--navy);
  }

  .headline {
    position: absolute;
    left: 36px; top: 118px;
    color: var(--orange);
    font-weight: 800;
    line-height: 1.02;
    -webkit-text-stroke: 1.5px var(--white);
    paint-order: stroke fill;
  }
  .headline__lead { display: block; font-size: 46px; }
  .headline__rest { display: block; font-size: 27px; }

  .headline-rule {
    position: absolute;
    left: 38px; top: 266px;
    width: 118px; height: 2px;
    background: var(--white);
  }

  .money-bag {
    position: absolute;
    left: 246px; top: 168px;
    width: 34px; height: 36px;
  }

  .services {
    position: absolute;
    left: 38px; top: 278px;
    list-style: none;
    color: var(--white);
    font-size: 10.5px;
    font-weight: 500;
  }
  .services li {
    display: flex; align-items: center; gap: 7px;
    height: 17px;
  }
  .services__icon {
    width: 13px; height: 13px; border-radius: 50%;
    background: var(--orange);
    border: 1.5px solid var(--white);
    flex: none;
  }

  .presenter {
    position: absolute;
    left: 330px; top: 58px;
    width: 150px; height: 250px;
    border-radius: 70px 70px 8px 8px;
    background: linear-gradient(180deg, #3b2a24 0%, #b8322b 35%, #8e1f1c 100%);
  }

  .pillars {
    position: absolute;
    right: 28px; bottom: 60px;
    list-style: none;
    color: var(--white);
    font-weight: 800;
    font-size: 13px;
    line-height: 1.15;
  }
  .pillars li { display: flex; align-items: center; gap: 6px; }
  .pillars li::before {
    content: ""; width: 6px; height: 6px; background: var(--navy);
  }
</style>
</head>
<body>

<section class="card card--front" aria-label="Flyer front">
  <svg class="card__art" viewBox="0 0 560 392" preserveAspectRatio="none">
    <defs>
      <linearGradient id="frontPhoto" x1="0" y1="0" x2="0.35" y2="1">
        <stop offset="0" stop-color="#9ccfcd"/>
        <stop offset="0.4" stop-color="#6e9c9f"/>
        <stop offset="0.75" stop-color="#1f3a5c"/>
        <stop offset="1" stop-color="#1b3453"/>
      </linearGradient>
    </defs>
    <rect width="560" height="392" fill="url(#frontPhoto)" role="img" aria-label="Photo of a modern white villa with large glass windows and trees"/>
    <path d="M0,392 L0,376 Q340,340 560,150 L560,392 Z" fill="var(--orange)"/>
    <path d="M0,368 Q340,332 560,142" fill="none" stroke="var(--white)" stroke-width="3"/>
  </svg>

  <div class="presenter" role="img" aria-label="Smiling man in a red blazer holding a model house"></div>

  <div class="brand-tab"><span class="brand-tab__dot"></span><span class="brand-tab__name">Dovrel</span></div>

  <h1 class="headline">
    <span class="headline__lead">Unlocking</span>
    <span class="headline__rest">Possibilities in</span>
    <span class="headline__rest">Real Estate</span>
    <span class="headline__rest">Financing</span>
  </h1>

  <svg class="money-bag" viewBox="0 0 34 36" aria-hidden="true">
    <path d="M12,8 L22,8 L19,12 C30,16 33,33 17,34 C1,33 4,16 15,12 Z" fill="var(--orange)" stroke="var(--white)" stroke-width="1.5"/>
    <text x="17" y="28" text-anchor="middle" font-family="Poppins, sans-serif" font-weight="800" font-size="12" fill="var(--white)">$</text>
  </svg>

  <div class="headline-rule"></div>

  <ul class="services">
    <li><span class="services__icon"></span>Project Financing</li>
    <li><span class="services__icon"></span>Temporary Real Estate Financing</li>
    <li><span class="services__icon"></span>Investiment Properties</li>
    <li><span class="services__icon"></span>Transformations</li>
  </ul>

  <ul class="pillars">
    <li>Fast</li>
    <li>Flexible</li>
    <li>Personal</li>
  </ul>
</section>

<section class="card card--back" aria-label="Flyer back">
  <svg class="card__art" viewBox="0 0 560 392" preserveAspectRatio="none">
    <defs>
      <linearGradient id="backPhoto" x1="0" y1="0" x2="0.35" y2="1">
        <stop offset="0" stop-color="#9ccfcd"/>
        <stop offset="0.4" stop-color="#6e9c9f"/>
        <stop offset="0.75" stop-color="#1f3a5c"/>
        <stop offset="1" stop-color="#1b3453"/>
      </linearGradient>
    </defs>
    <rect width="560" height="392" fill="url(#backPhoto)" role="img" aria-label="Photo of a modern white villa with large glass windows and trees"/>
    <path d="M0,392 L0,376 Q340,340 560,150 L560,392 Z" fill="var(--orange)"/>
    <path d="M0,368 Q340,332 560,142" fill="none" stroke="var(--white)" stroke-width="3"/>
  </svg>

  <div class="brand-tab"><span class="brand-tab__dot"></span><span class="brand-tab__name">Dovrel</span></div>

  <ul class="pillars">
    <li>Fast</li>
    <li>Flexible</li>
    <li>Personal</li>
  </ul>
</section>

</body>
</html>
```